Business Card Design Project

Company name will be Tallow Crest (named after my black lab and his fraying muzzle) Business is in the body armor, Security product industry servicing the state, local, and federal law enforcement markets. I want a more formal and serious logo for both business cards and letterhead

```html
<!DOCTYPE html>
<html lang="en">
<head>
<meta charset="utf-8">
<title>Tallow Crest — Business Card and Letterhead</title>
<link rel="stylesheet" href="https://fonts.googleapis.com/css2?family=Anton&family=Oswald:wght@600&display=swap">
<style>
  :root {
    --canvas-bg: #ffffff;
    --card-grey: #b5b5b5;
    --frame-grey: #9c9c9c;
    --sheet-white: #ffffff;
    --shadow: rgba(0, 0, 0, 0.45);
    --ink: #2b2b2b;
  }
  * { margin: 0; padding: 0; box-sizing: border-box; }
  html, body {
    width: 1200px;
    height: 1035px;
    overflow: hidden;
    background: var(--canvas-bg);
  }
  .canvas {
    position: relative;
    width: 1200px;
    height: 1035px;
  }

  /* Business card */
  .business-card {
    position: absolute;
    left: 7px;
    top: 7px;
    width: 363px;
    height: 207px;
    background: var(--card-grey);
    box-shadow: 4px 5px 6px var(--shadow);
    color: var(--ink);
  }
  .card-person {
    position: absolute;
    left: 17px;
    top: 24px;
    font-family: "Oswald", "Arial Narrow", sans-serif;
    font-weight: 600;
    font-size: 11px;
    line-height: 19px;
  }
  .card-contact {
    position: absolute;
    right: 18px;
    top: 24px;
    text-align: right;
    font-family: "Oswald", "Arial Narrow", sans-serif;
    font-weight: 600;
    font-size: 10.5px;
    line-height: 18.5px;
  }
  .card-wordmark {
    position: absolute;
    left: 16px;
    bottom: 10px;
    font-family: "Anton", "Impact", sans-serif;
    font-size: 64px;
    line-height: 1;
    white-space: nowrap;
    letter-spacing: -0.5px;
  }

  /* Letterhead */
  .letterhead {
    position: absolute;
    left: 399px;
    top: 9px;
    width: 783px;
    height: 1007px;
    background: var(--frame-grey);
    box-shadow: 4px 5px 6px var(--shadow);
    padding: 12px 13px 14px 13px;
  }
  .letterhead-sheet {
    position: relative;
    width: 100%;
    height: 100%;
    background: var(--sheet-white);
    color: var(--ink);
  }
  .letterhead-footer {
    position: absolute;
    right: 20px;
    bottom: 22px;
    text-align: right;
  }
  .letterhead-wordmark {
    font-family: "Anton", "Impact", sans-serif;
    font-size: 33px;
    line-height: 1.1;
    white-space: nowrap;
    margin-bottom: 10px;
  }
  .letterhead-contact {
    font-family: "Oswald", "Arial Narrow", sans-serif;
    font-weight: 600;
    font-size: 10px;
    line-height: 19px;
  }
</style>
</head>
<body>
<main class="canvas">
  <section class="business-card" aria-label="Business card">
    <div class="card-person">
      <p class="person-name">Reid Calloway</p>
      <p class="person-role">Manufacturers Rep Principal</p>
    </div>
    <address class="card-contact" style="font-style: normal;">
      <p>4710 Harbor Lane East</p>
      <p>Marlow Point, FL 32900</p>
      <p>(c) 555-014-2270</p>
      <p>rcalloway@mailbox.example</p>
    </address>
    <p class="card-wordmark">Tallow Crest</p>
  </section>

  <section class="letterhead" aria-label="Letterhead">
    <div class="letterhead-sheet">
      <footer class="letterhead-footer">
        <p class="letterhead-wordmark">Tallow Crest</p>
        <address class="letterhead-contact" style="font-style: normal;">
          <p>4710 Harbor Lane East</p>
          <p>Marlow Point, FL 32900</p>
          <p>(c) 555-014-2270</p>
          <p>rcalloway@mailbox.example</p>
        </address>
      </footer>
    </div>
  </section>
</main>
</body>
</html>
```